Business card to promote business guidance

I need a card design to give to all my customers advertising a way to build a business exactly like the one they just bought from. I have an online store and will include one with each shipment. It should state the way to financial freedom and working for yourself

Target Market(s)

Young Entrepreneurs that want to start and don't know how

Industry/Entity Type

Business

Contact Information for Business Card

"You just bought from a successful company on Vorpex. I have a unique business model, discovered by me, unlike any other that can make anyone successful. Follow me and message me for exactly the same model. If you ever wanted to work for yourself, I will teach you how. It's not a pipe dream, allow me to guide you out of the box."

Colors
85abd2

Requirements
Must have
• website www.loganmerewick.com
instagram @theloganmerewick

```html
<!DOCTYPE html>
<html lang="en">
<head>
<meta charset="utf-8">
<title>Logan Merewick – Business Card</title>
<link href="https://fonts.googleapis.com/css2?family=Open+Sans:ital,wght@0,400;0,600;0,700;1,700&display=swap" rel="stylesheet">
<style>
  :root {
    --brand: #85abd2;
    --brand-deep: #6f97c6;
    --brand-light: #9dbde0;
    --paper: #ffffff;
    --ink-light: #ffffff;
    --backdrop: #e9edf2;
  }
  * { box-sizing: border-box; margin: 0; padding: 0; }
  html, body {
    width: 1200px; height: 900px; overflow: hidden;
    background: var(--backdrop);
    font-family: "Open Sans", Arial, sans-serif;
  }
  .sheet {
    position: relative; width: 1200px; height: 900px;
    display: flex; flex-direction: column; align-items: center; justify-content: center; gap: 44px;
  }
  .card {
    position: relative; width: 620px; height: 354px; overflow: hidden;
    box-shadow: 0 8px 24px rgba(40, 60, 90, 0.18);
  }

  /* Front */
  .card-front { background: var(--paper); color: var(--brand); }
  .front-name {
    position: absolute; top: 40px; left: 0; width: 100%;
    text-align: center; font-weight: 700; font-style: italic; font-size: 30px; letter-spacing: 0.5px;
    text-transform: uppercase;
  }
  .front-role {
    position: absolute; top: 82px; left: 0; width: 100%;
    text-align: center; font-weight: 600; font-size: 15px;
  }
  .front-rule {
    position: absolute; top: 108px; left: 230px; width: 160px; height: 2px; background: var(--brand);
  }
  .front-icons {
    position: absolute; top: 120px; left: 0; width: 100%;
    display: flex; justify-content: center; gap: 10px;
  }
  .front-icons svg { width: 14px; height: 14px; }
  .front-contacts {
    position: absolute; top: 142px; left: 0; width: 100%;
    text-align: center; font-size: 13px; line-height: 19px; font-weight: 600;
  }
  .tagline-bar {
    position: absolute; top: 218px; left: 36px; width: 548px; height: 32px;
    border-radius: 16px; background: var(--brand);
    color: var(--ink-light); font-weight: 700; font-size: 17px; letter-spacing: 0.8px;
    display: flex; align-items: center; justify-content: center;
  }
  .tagline-sub {
    position: absolute; top: 262px; left: 0; width: 100%;
    display: flex; align-items: center; justify-content: center; gap: 14px;
    font-weight: 700; font-size: 15px; letter-spacing: 0.8px;
  }
  .tagline-sub svg { width: 70px; height: 14px; }

  /* Back */
  .card-back {
    background: linear-gradient(160deg, var(--brand-light) 0%, var(--brand) 55%, var(--brand-deep) 100%);
    color: var(--ink-light);
  }
  .back-emblem {
    position: absolute; left: 120px; top: 70px; width: 230px; height: 210px;
    border-radius: 50%;
    background: radial-gradient(circle, rgba(70, 100, 140, 0.22), rgba(70, 100, 140, 0) 70%);
  }
  .back-quote {
    position: absolute; top: 44px; left: 40px; right: 40px;
    text-align: center; font-weight: 600; font-size: 16.5px; line-height: 25px;
  }
  .back-signature {
    position: absolute; top: 278px; left: 0; width: 100%;
    text-align: center; font-weight: 700; font-size: 24px; letter-spacing: 0.5px;
  }
</style>
</head>
<body>
<main class="sheet">

  <section class="card card-front" aria-label="Card front">
    <h1 class="front-name">Logan Merewick</h1>
    <p class="front-role">Owner</p>
    <div class="front-rule"></div>
    <div class="front-icons">
      <svg viewBox="0 0 14 14" aria-label="Phone"><path d="M3 1.5l2 2.2-1 1.3c.8 1.8 2.2 3.2 4 4l1.3-1 2.2 2-1.2 1.8C6 11.5 2.5 8 1.2 2.7z" fill="var(--brand)"/></svg>
      <svg viewBox="0 0 14 14" aria-label="Website"><circle cx="7" cy="7" r="6" fill="none" stroke="var(--brand)" stroke-width="1.4"/><ellipse cx="7" cy="7" rx="2.6" ry="6" fill="none" stroke="var(--brand)" stroke-width="1.2"/><line x1="1" y1="7" x2="13" y2="7" stroke="var(--brand)" stroke-width="1.2"/></svg>
      <svg viewBox="0 0 14 14" aria-label="Social profile"><rect x="1.5" y="1.5" width="11" height="11" rx="2" fill="var(--brand)"/></svg>
    </div>
    <div class="front-contacts">
      <p>123 456 7890</p>
      <p>www.loganmerewick.com</p>
      <p>@theloganmerewick</p>
    </div>
    <div class="tagline-bar">The way to financial freedom</div>
    <div class="tagline-sub">
      <svg viewBox="0 0 70 14"><polygon points="0,0 70,7 0,14 14,7" fill="var(--brand)"/></svg>
      <span>Working for yourself</span>
      <svg viewBox="0 0 70 14"><polygon points="70,0 0,7 70,14 56,7" fill="var(--brand)"/></svg>
    </div>
  </section>

  <section class="card card-back" aria-label="Card back">
    <div class="back-emblem" role="img" aria-label="Faint brand emblem in the background"></div>
    <p class="back-quote">"You just bought from a successful company on Vorpex. I have a unique business model, discovered by me, unlike any other that can make anyone successful. Follow me and message me for exactly the same model. If you ever wanted to work for yourself, I will teach you how. It's not a pipe dream, allow me to guide you out of the box."</p>
    <p class="back-signature">- LOGAN MEREWICK</p>
  </section>

</main>
</body>
</html>
```